Update Website, Include new Logo

We are a Technology Managed Service Provider (MSP)
+cyber security company operating out of New York City and New Jersey. Our main customer base has been financial service industry, high tech, multi-media, and/or other enterprise level customers. Current website is very old but still valid from an offering standpoint but we now want to emphasize and focus more on Cyber Security. We are offering a new cybersecurity line targeted at offering NGOs, Government, and Small-Mid Sized businesses the same level of cybersecurity as big business.

We would like to incorporate the new Pravlin logo and keep the feel modern, secure (without feeling aggressive). We want our clients to feel we will offer them white glove service at affordable cost - safety, security and stability are attainable at all levels.

I am attaching logos for visual, as you need copy, please let us know and we can send you the verbiage. Our current site is www.pravlin-example.com for comparison

Target Market(s)

Any businesses who need cyber security

Industry/Entity Type

Technology - Cybersecurity

Number of Pages Required

3 page

Colors
0054AA
0677BA
7BADD7
CADEEF
E8F1F8
FFC000
F8CF3A
FAE287
FDF2CF
FEFAEE
F0912C
F2A743
F7CA91
FBE8D2
FDF5EE
EE7325
F08F49
F5BC92
FAE3D3
FDF4ED

Requirements
Must have
• Bulleted points about SOC, compliance, Ambrolite, etc (see marketing doc). Please use the new Pravlin Logo (in zip), we like the orange version (with the fading color). Would like to have that color be included throughout, however do not want it to be childish. Open to ideas on colors/layout/imagery
Nice to have
• An area to capture customer data (schedule a Penetration Test, ask for more info, or check pricing), or a link/qr code area we can add that
Should not have
• Halloween feel, An aggressive feel, hard sell. Not large areas of paragraphs (like our current page).

```html
<!DOCTYPE html>
<html lang="en">
<head>
<meta charset="utf-8">
<title>Pravlin Technology — Cybersecurity</title>
<link href="https://fonts.googleapis.com/css2?family=Poppins:wght@400;500;600;700&display=swap" rel="stylesheet">
<style>
:root{
  --orange:#EE7325;
  --orange-2:#F0912C;
  --yellow:#FFC000;
  --navy:#0a2a6e;
  --blue:#0054AA;
  --blue-2:#0677BA;
  --sky:#7BADD7;
  --ice:#E8F1F8;
  --ink:#111;
  --text:#333;
  --white:#fff;
  --grad:linear-gradient(90deg,var(--orange),var(--orange-2) 45%,var(--yellow));
}
*{box-sizing:border-box;margin:0;padding:0}
html,body{width:1200px;height:3951px;overflow:hidden}
body{font-family:"Poppins",sans-serif;color:var(--text);background:var(--white);position:relative}
section,header,footer{position:absolute;left:0;width:1200px;overflow:hidden}
.abs{position:absolute}
.btn{position:absolute;display:flex;align-items:center;justify-content:center;background:var(--grad);color:var(--white);font-weight:700;font-size:15px;text-transform:uppercase;
  clip-path:polygon(14px 0,calc(100% - 14px) 0,100% 50%,calc(100% - 14px) 100%,14px 100%,0 50%)}
.rule{position:absolute;height:3px;width:60px;background:var(--grad)}
.h2{position:absolute;font-weight:700;font-size:31px;color:var(--ink);text-transform:uppercase;letter-spacing:.3px}

/* header */
.site-header{top:0;height:95px;background:var(--white);z-index:3;overflow:visible}
.topbar{position:absolute;left:383px;top:0;width:817px;height:46px;background:var(--grad);clip-path:polygon(0 0,100% 0,100% 100%,30px 100%)}
.topbar-item{position:absolute;top:0;height:46px;display:flex;align-items:center;gap:14px;color:var(--white);font-size:15px;font-weight:500;white-space:nowrap}
.topbar-item b{font-weight:700}
.ico-circle{width:34px;height:34px;border-radius:50%;background:var(--white);display:flex;align-items:center;justify-content:center}
.brand-tab{position:absolute;left:92px;top:0;width:188px;height:118px;background:var(--white);clip-path:polygon(0 0,100% 0,100% 82%,88% 100%,12% 100%,0 82%);display:flex;align-items:center;justify-content:center}
.brand-name{font-weight:700;font-size:31px;color:var(--ink);letter-spacing:.5px}
.main-nav{position:absolute;top:59px;left:0;width:1200px;height:24px}
.main-nav a{position:absolute;font-size:15px;font-weight:500;color:var(--ink);text-decoration:none;white-space:nowrap}
.main-nav a.active{color:var(--orange)}

/* hero */
.hero{top:95px;height:566px;background:radial-gradient(circle at 838px 283px,#3fb8ff 0,#1466c8 120px,#0b3a96 260px,#08266e 520px)}
.hero h1{position:absolute;left:107px;top:140px;font-size:49px;line-height:61px;color:var(--white);font-weight:700;text-transform:uppercase;white-space:nowrap}
.hero p{position:absolute;left:107px;top:327px;font-size:14.5px;line-height:27px;color:var(--white);white-space:nowrap}

/* about */
.about{top:661px;height:579px;background:var(--white)}
.about-panel{position:absolute;left:0;top:0;width:499px;height:579px;background:linear-gradient(160deg,#1c5fae,#0c3a7d);clip-path:polygon(0 0,100% 0,288px 100%,0 100%)}
.hex-figure{position:absolute}
.bullets{position:absolute;list-style:none}
.bullets li{position:relative;padding-left:27px;font-size:14.5px;line-height:21px;color:var(--text)}
.bullets li svg{position:absolute;left:0;top:3px}

/* solution */
.solution{top:1240px;height:621px;background:var(--ice)}
.center{left:0;width:1200px;text-align:center}
.sol-item{position:absolute;top:214px;width:220px}
.sol-icon{width:92px;height:92px}
.sol-item h3{margin-top:23px;font-size:15px;line-height:25px;font-weight:600;color:var(--ink);text-transform:uppercase}
.sol-item p{margin-top:11px;font-size:14px;line-height:23px;color:var(--text)}

/* advantage */
.advantage{top:1861px;height:613px;background:var(--white)}
.adv-list li{line-height:32px;padding-left:29px}
.adv-list li svg{top:7px}

/* tech */
.tech{top:2474px;height:440px;background:linear-gradient(180deg,#1b55a8,#164c9c)}
.tech-item{position:absolute;top:181px;width:300px;text-align:center}
.tech-circle{width:92px;height:92px;border-radius:50%;background:var(--white);margin:0 auto;display:flex;align-items:center;justify-content:center}
.tech-item p{margin-top:14px;color:var(--white);font-size:15px;line-height:27px}

/* contact */
.contact{top:2914px;height:618px;background:var(--white)}
.contact-card{position:absolute;left:110px;top:107px;width:459px;height:398px;background:var(--white);box-shadow:0 4px 22px rgba(0,0,0,.1)}
.field{position:absolute;left:45px;width:367px;border:1px solid #cfcfcf;font-size:14px;color:#444;padding:12px 14px;font-family:inherit}
.info-item{position:absolute;left:634px}
.info-icon{position:absolute;left:0;top:0;width:48px;height:48px;border-radius:50%;background:var(--grad);display:flex;align-items:center;justify-content:center}
.info-text{position:absolute;left:66px;top:0;width:420px;font-size:16px;line-height:27px;color:var(--text)}
.info-text b{display:block;font-weight:500;color:var(--ink);font-size:17px}

/* footer */
.site-footer{top:3532px;height:419px;background:#000}
.footer-brand{position:absolute;left:0;width:1200px;top:150px;text-align:center;font-weight:700;font-size:56px;color:var(--orange);letter-spacing:1px}
.footer-nav{position:absolute;top:278px;left:0;width:1200px;display:flex;justify-content:center;gap:33px}
.footer-nav a{color:var(--white);font-size:15px;text-decoration:none}
.copyright{position:absolute;top:337px;left:0;width:1200px;text-align:center;color:var(--white);font-size:15px}
</style>
</head>
<body>

<header class="site-header">
  <div class="topbar">
    <div class="topbar-item" style="left:113px">
      <span class="ico-circle"><svg width="16" height="16" viewBox="0 0 24 24"><path fill="#EE7325" d="M6.6 10.8a15 15 0 0 0 6.6 6.6l2.2-2.2c.3-.3.7-.4 1-.2 1.1.4 2.3.6 3.6.6.6 0 1 .4 1 1V20c0 .6-.4 1-1 1A17 17 0 0 1 3 4c0-.6.4-1 1-1h3.5c.6 0 1 .4 1 1 0 1.3.2 2.5.6 3.6.1.3 0 .7-.2 1z"/></svg></span>
      <span><b>PHONE:</b> (212) 555-0147</span>
    </div>
    <div class="topbar-item" style="left:406px">
      <span class="ico-circle"><svg width="16" height="16" viewBox="0 0 24 24"><path fill="#EE7325" d="M3 5h18v14H3z"/><path fill="none" stroke="#fff" stroke-width="2" d="M3 6l9 7 9-7"/></svg></span>
      <span><b>E-MAIL:</b> Support@pravlin-example.com</span>
    </div>
  </div>
  <div class="brand-tab"><span class="brand-name">PRAVLIN</span></div>
  <nav class="main-nav">
    <a class="active" style="left:460px">HOME</a>
    <a style="left:543px">ABOUT US</a>
    <a style="left:657px">SERVICES</a>
    <a style="left:766px">PROBLEM</a>
    <a style="left:873px">SOLUTION</a>
    <a style="left:985px">CONTACT US</a>
  </nav>
</header>

<section class="hero" role="img" aria-label="Glowing digital security network with circuit lines and connected device icons around a central shield">
  <h1>Protecting Data.<br>Empowering<br>Organizations.</h1>
  <p>Internal AI agents for workflow efficiency to boost response<br>times, team productivity, and performance analytics.</p>
  <div class="btn" style="left:107px;top:399px;width:315px;height:46px">Schedule a Penetration Test</div>
</section>

<section class="about">
  <div class="about-panel"></div>
  <svg class="hex-figure" style="left:107px;top:106px" width="392" height="400" viewBox="0 0 392 400">
    <defs><linearGradient id="hexline" x1="0" x2="1"><stop offset="0" stop-color="#EE7325"/><stop offset="1" stop-color="#FFC000"/></linearGradient>
    <radialGradient id="aboutfill" cx=".5" cy=".5" r=".6"><stop offset="0" stop-color="#5fc4ff"/><stop offset=".4" stop-color="#1a62c4"/><stop offset="1" stop-color="#061c4d"/></radialGradient></defs>
    <polygon points="196,4 388,104 388,296 196,396 4,296 4,104" fill="none" stroke="url(#hexline)" stroke-width="3"/>
    <polygon points="196,16 376,110 376,290 196,384 16,290 16,110" fill="none" stroke="url(#hexline)" stroke-width="3"/>
    <polygon points="196,28 364,116 364,284 196,372 28,284 28,116" fill="url(#aboutfill)" role="img" aria-label="Digital padlock surrounded by glowing security icons"/>
  </svg>
  <div class="h2" style="left:615px;top:100px">About Us</div>
  <div class="rule" style="left:615px;top:152px;width:77px"></div>
  <ul class="bullets" style="left:615px;top:191px;width:480px">
    <li style="margin-bottom:22px"><svg width="16" height="16" viewBox="0 0 16 16"><polygon points="8,1 14,4.5 14,11.5 8,15 2,11.5 2,4.5" fill="none" stroke="#333" stroke-width="2"/><circle cx="8" cy="8" r="2" fill="#333"/></svg>Cyberattacks cost organizations $4.4M on average per breach; SMBs face nearly $1M in recovery costs.</li>
    <li style="margin-bottom:22px"><svg width="16" height="16" viewBox="0 0 16 16"><polygon points="8,1 14,4.5 14,11.5 8,15 2,11.5 2,4.5" fill="none" stroke="#333" stroke-width="2"/><circle cx="8" cy="8" r="2" fill="#333"/></svg>SaaS reliance creates data loss risks (70% of organizations experience SaaS data disruptions).</li>
    <li style="margin-bottom:22px"><svg width="16" height="16" viewBox="0 0 16 16"><polygon points="8,1 14,4.5 14,11.5 8,15 2,11.5 2,4.5" fill="none" stroke="#333" stroke-width="2"/><circle cx="8" cy="8" r="2" fill="#333"/></svg>Cyber insurance is increasingly costly and complex.</li>
    <li><svg width="16" height="16" viewBox="0 0 16 16"><polygon points="8,1 14,4.5 14,11.5 8,15 2,11.5 2,4.5" fill="none" stroke="#333" stroke-width="2"/><circle cx="8" cy="8" r="2" fill="#333"/></svg>Nonprofits and government orgs are high-value targets with limited cyber resources.</li>
  </ul>
  <div class="btn" style="left:615px;top:422px;width:143px;height:49px">Read More</div>
</section>

<section class="solution">
  <div class="h2 center" style="top:96px">Our Solution</div>
  <div class="rule" style="left:565px;top:144px;width:70px"></div>
  <div class="abs center" style="top:166px;font-size:16px;color:var(--ink)">Pravlin Security Ecosystem</div>

  <div class="sol-item" style="left:110px">
    <svg class="sol-icon" viewBox="0 0 92 92"><polygon points="46,3 85,25 85,67 46,89 7,67 7,25" fill="#fff" stroke="#cfd9e6" stroke-width="2"/><rect x="30" y="32" width="32" height="22" rx="2" fill="none" stroke="#1b55a8" stroke-width="2.5"/><path d="M40 60h12M46 54v6" stroke="#1b55a8" stroke-width="2.5"/></svg>
    <h3>Managed SOC<br>(24/7/365)</h3>
    <p>Advanced threat detection<br>across endpoint, network,<br>and cloud.</p>
  </div>
  <div class="sol-item" style="left:376px">
    <svg class="sol-icon" viewBox="0 0 92 92"><polygon points="46,3 85,25 85,67 46,89 7,67 7,25" fill="#fff" stroke="#cfd9e6" stroke-width="2"/><path d="M32 54a9 9 0 0 1 2-18 12 12 0 0 1 23-2 10 10 0 0 1 3 20z" fill="none" stroke="#1b55a8" stroke-width="2.5"/><path d="M46 54v8M40 62h12" stroke="#1b55a8" stroke-width="2.5"/></svg>
    <h3>SaaS<br>Protection</h3>
    <p>3x daily backups, infinite<br>retention, fast restores,<br>ransomware rollback.</p>
  </div>
  <div class="sol-item" style="left:641px">
    <svg class="sol-icon" viewBox="0 0 92 92"><polygon points="46,3 85,25 85,67 46,89 7,67 7,25" fill="#1b55a8"/><rect x="28" y="32" width="36" height="24" rx="2" fill="none" stroke="#fff" stroke-width="2.5"/><path d="M40 62h12M46 56v6" stroke="#fff" stroke-width="2.5"/><path d="M52 26l6 2v5c0 4-3 6-6 7-3-1-6-3-6-7v-5z" fill="#1b55a8" stroke="#fff" stroke-width="2"/></svg>
    <h3>Fast Track<br>Cyber Insurance</h3>
    <p>Pre-qualified $1.5M cyber<br>liability coverage via<br>Ambrolite partnership.</p>
  </div>
  <div class="sol-item" style="left:907px">
    <svg class="sol-icon" viewBox="0 0 92 92"><polygon points="46,3 85,25 85,67 46,89 7,67 7,25" fill="#fff" stroke="#cfd9e6" stroke-width="2"/><rect x="30" y="34" width="32" height="24" fill="none" stroke="#1b55a8" stroke-width="2.5"/><path d="M30 36l16 12 16-12" fill="none" stroke="#1b55a8" stroke-width="2.5"/></svg>
    <h3>Awareness &amp;<br>Phishing Defense</h3>
    <p>AI-powered email security,<br>training,and simulations.</p>
  </div>
  <div class="btn" style="left:523px;top:491px;width:152px;height:49px">View More</div>
</section>

<section class="advantage">
  <div class="h2" style="left:112px;top:104px">Competitive Advantage</div>
  <div class="rule" style="left:112px;top:155px;width:66px"></div>
  <ul class="bullets adv-list" style="left:112px;top:183px;width:460px">
    <li><svg width="18" height="18" viewBox="0 0 16 16"><polygon points="8,1 14,4.5 14,11.5 8,15 2,11.5 2,4.5" fill="none" stroke="#F0912C" stroke-width="2"/><circle cx="8" cy="8" r="2" fill="#FFC000"/></svg>Integrated stack (Backup + SOC + Cyber Insurance + Awareness + Support).</li>
    <li><svg width="18" height="18" viewBox="0 0 16 16"><polygon points="8,1 14,4.5 14,11.5 8,15 2,11.5 2,4.5" fill="none" stroke="#F0912C" stroke-width="2"/><circle cx="8" cy="8" r="2" fill="#FFC000"/></svg>Compliance-ready (SOC2, GDPR, HIPAA).</li>
    <li><svg width="18" height="18" viewBox="0 0 16 16"><polygon points="8,1 14,4.5 14,11.5 8,15 2,11.5 2,4.5" fill="none" stroke="#F0912C" stroke-width="2"/><circle cx="8" cy="8" r="2" fill="#FFC000"/></svg>Financial safety net via Ambrolite: $500K warranty + $1M insurance.</li>
    <li><svg width="18" height="18" viewBox="0 0 16 16"><polygon points="8,1 14,4.5 14,11.5 8,15 2,11.5 2,4.5" fill="none" stroke="#F0912C" stroke-width="2"/><circle cx="8" cy="8" r="2" fill="#FFC000"/></svg>Differentiated branding: trust, protection, knowledge—not fear.</li>
    <li><svg width="18" height="18" viewBox="0 0 16 16"><polygon points="8,1 14,4.5 14,11.5 8,15 2,11.5 2,4.5" fill="none" stroke="#F0912C" stroke-width="2"/><circle cx="8" cy="8" r="2" fill="#FFC000"/></svg>Flexibility in service offerings and agreements.</li>
  </ul>
  <div class="btn" style="left:112px;top:456px;width:152px;height:46px">View More</div>
  <svg class="hex-figure" style="left:640px;top:126px" width="390" height="400" viewBox="0 0 390 400">
    <defs><linearGradient id="hexline2" x1="0" x2="1"><stop offset="0" stop-color="#EE7325"/><stop offset="1" stop-color="#FFC000"/></linearGradient>
    <radialGradient id="advfill" cx=".5" cy=".45" r=".6"><stop offset="0" stop-color="#8fd6ff"/><stop offset=".35" stop-color="#2a6fb8"/><stop offset="1" stop-color="#0b1c38"/></radialGradient></defs>
    <polygon points="195,3 387,104 387,296 195,397 3,296 3,104" fill="none" stroke="url(#hexline2)" stroke-width="3"/>
    <polygon points="195,14 376,110 376,290 195,386 14,290 14,110" fill="none" stroke="url(#hexline2)" stroke-width="3"/>
    <polygon points="195,26 364,116 364,284 195,374 26,284 26,116" fill="url(#advfill)" role="img" aria-label="Glowing digital padlock resting on a circuit board"/>
  </svg>
</section>

<section class="tech">
  <div class="h2 center" style="top:78px;color:var(--white)">Technology &amp; AI Integration</div>
  <div class="rule" style="left:565px;top:128px;width:70px"></div>
  <svg class="abs" style="left:0;top:0" width="1200" height="440">
    <path d="M312 220 C 400 170, 500 170, 550 215" fill="none" stroke="#fff" stroke-width="2" stroke-dasharray="2 5"/>
    <path d="M646 228 C 720 270, 820 270, 888 215" fill="none" stroke="#fff" stroke-width="2" stroke-dasharray="2 5"/>
  </svg>
  <div class="tech-item" style="left:114px">
    <div class="tech-circle"><svg width="44" height="44" viewBox="0 0 44 44"><rect x="6" y="14" width="32" height="22" fill="none" stroke="#1b55a8" stroke-width="2.5"/><path d="M6 16l16 12 16-12" fill="none" stroke="#1b55a8" stroke-width="2.5"/><rect x="17" y="6" width="10" height="10" rx="2" fill="none" stroke="#1b55a8" stroke-width="2"/></svg></div>
    <p>AI-powered phishing detection<br>and email security</p>
  </div>
  <div class="tech-item" style="left:448px">
    <div class="tech-circle"><svg width="44" height="44" viewBox="0 0 44 44"><path d="M22 6l13 5v9c0 9-6 14-13 17-7-3-13-8-13-17v-9z" fill="none" stroke="#1b55a8" stroke-width="2.5"/><path d="M16 22l4 4 8-8" fill="none" stroke="#1b55a8" stroke-width="2.5"/></svg></div>
    <p>AI-driven SOC analytics and<br>automation.</p>
  </div>
  <div class="tech-item" style="left:784px">
    <div class="tech-circle"><svg width="44" height="44" viewBox="0 0 44 44"><rect x="10" y="16" width="24" height="18" rx="4" fill="none" stroke="#1b55a8" stroke-width="2.5"/><circle cx="17" cy="25" r="2" fill="#1b55a8"/><circle cx="27" cy="25" r="2" fill="#1b55a8"/><path d="M22 16v-6M18 8h8M6 22v6M38 22v6" stroke="#1b55a8" stroke-width="2.5"/></svg></div>
    <p>Internal AI agents for workflow<br>efficiency to boost response</p>
  </div>
</section>

<section class="contact">
  <form class="contact-card">
    <div class="h2" style="left:43px;top:29px">Contact Us</div>
    <div class="field" style="top:83px;height:48px">Name</div>
    <div class="field" style="top:147px;height:48px">Email</div>
    <div class="field" style="top:211px;height:85px">Message</div>
    <div class="btn" style="left:47px;top:316px;width:116px;height:46px">Submit</div>
  </form>

  <div class="h2" style="left:634px;top:128px">Contact Information</div>
  <div class="rule" style="left:634px;top:178px;width:70px"></div>

  <div class="info-item" style="top:225px">
    <div class="info-icon"><svg width="20" height="20" viewBox="0 0 24 24"><path fill="#fff" d="M6.6 10.8a15 15 0 0 0 6.6 6.6l2.2-2.2c.3-.3.7-.4 1-.2 1.1.4 2.3.6 3.6.6.6 0 1 .4 1 1V20c0 .6-.4 1-1 1A17 17 0 0 1 3 4c0-.6.4-1 1-1h3.5c.6 0 1 .4 1 1 0 1.3.2 2.5.6 3.6.1.3 0 .7-.2 1z"/></svg></div>
    <div class="info-text" style="top:-4px"><b>PHONE:</b>(212) 555-0147</div>
  </div>
  <div class="info-item" style="top:321px">
    <div class="info-icon"><svg width="20" height="20" viewBox="0 0 24 24"><path fill="#fff" d="M3 5h18v14H3z"/><path fill="none" stroke="#F0912C" stroke-width="2" d="M3 6l9 7 9-7"/></svg></div>
    <div class="info-text" style="top:-4px"><b>E-MAIL:</b>SUPPORT@PRAVLIN-EXAMPLE.COM</div>
  </div>
  <div class="info-item" style="top:416px">
    <div class="info-icon"><svg width="20" height="20" viewBox="0 0 24 24"><path fill="#fff" d="M12 2a7 7 0 0 0-7 7c0 5 7 13 7 13s7-8 7-13a7 7 0 0 0-7-7zm0 9.5A2.5 2.5 0 1 1 12 6.5a2.5 2.5 0 0 1 0 5z"/></svg></div>
    <div class="info-text" style="top:-4px"><b>ADDRESS:</b>HEADQUARTERS 1480 HARBOR AVENUE<br>SUITE 410 NEW YORK, NY 10036</div>
  </div>
</section>

<footer class="site-footer">
  <div class="footer-brand">PRAVLIN</div>
  <nav class="footer-nav">
    <a>HOME</a><a>ABOUT US</a><a>SERVICES</a><a>PROBLEM</a><a>SOLUTION</a><a>CONTACT US</a>
  </nav>
  <div class="copyright">COPYRIGHTS@2025.COMPANY NAME.ALL RIGHTS RESERVED</div>
</footer>

</body>
</html>
```